Help keep hoosiers happy and at home!

We need a billboard designed for our Indiana based healthcare business called 'Harbor Lane Home Aides'. We administer a medicaid waiver program that provides support and financial aid to live in caregivers that take care of someone who would otherwise be in a nursing home or skilled nursing facility. Qualified caregivers could be eligible to receive up to 1200 dollars a month in tax free financial aid, as well as access to nursing support that helps manage any unexpected situations or changes in a care recipients condition or care routine. Our program empowers families to keep their loved ones at home and out of the nursing home. NOTE: We believe the tagline at the bottom of our logo is disproportionately small. We would like to see that tagline larger and easier to read. I look forward to seeing your design ideas!

Target Market(s)

Medicaid aged beneficiaries and caregivers.

Industry/Entity Type

Home Healthcare

Colors
0054AA
0677BA
7BADD7
CADEEF
E8F1F8

Requirements
Nice to have
• "Empowering friends and family to care for their loves ones at home. Eligible participants receive up to $15,000 a year, tax free."

```html
<!DOCTYPE html>
<html lang="en">
<head>
<meta charset="utf-8">
<title>Harbor Lane Home Aides — Billboard</title>
<link rel="stylesheet" href="https://fonts.googleapis.com/css2?family=Montserrat:wght@400;500;600&display=swap">
<style>
  :root {
    --page-bg: #e4e4e6;
    --navy: #172a78;
    --sky-blue: #1f7bc8;
    --pill-blue: #1f74c4;
    --white: #ffffff;
    --brand-navy: #172a78;
  }
  html, body {
    margin: 0;
    padding: 0;
    width: 1119px;
    height: 1200px;
    overflow: hidden;
    background: var(--page-bg);
  }
  .canvas {
    position: relative;
    width: 1119px;
    height: 1200px;
  }
  .billboard {
    position: absolute;
    left: 40px;
    top: 426px;
    width: 1039px;
    height: 348px;
    filter: drop-shadow(0 10px 12px rgba(0,0,0,0.35));
  }
  .billboard svg { display: block; }
  .sans { font-family: "Montserrat", Arial, sans-serif; }
  .headline { font-weight: 600; font-size: 40px; fill: var(--white); }
  .lead { font-weight: 500; font-size: 24.5px; fill: var(--white); }
  .pill-label { font-weight: 500; font-size: 18px; fill: var(--white); letter-spacing: 0.3px; }
  .phone { font-weight: 600; font-size: 47px; fill: var(--white); letter-spacing: -0.5px; }
  .web { font-weight: 500; font-size: 16.5px; fill: var(--white); }
  .slogan { font-weight: 600; font-size: 31px; fill: var(--white); }
  .offer { font-weight: 500; font-size: 22.5px; fill: var(--white); }
  .amount { font-weight: 600; font-size: 72px; fill: var(--white); letter-spacing: -1.5px; }
  .terms { font-weight: 500; font-size: 25px; fill: var(--white); }
  .brand-name { font-weight: 600; font-size: 24px; fill: var(--brand-navy); }
</style>
</head>
<body>
<main class="canvas">
  <section class="billboard" aria-label="Harbor Lane Home Aides billboard">
    <svg width="1039" height="348" viewBox="0 0 1039 348" xmlns="http://www.w3.org/2000/svg">
      <defs>
        <filter id="badge-shadow" x="-20%" y="-20%" width="140%" height="140%">
          <feDropShadow dx="0" dy="3" stdDeviation="5" flood-color="#000" flood-opacity="0.35"/>
        </filter>
        <clipPath id="board-clip"><rect width="1039" height="348"/></clipPath>
      </defs>
      <g clip-path="url(#board-clip)">
        <rect class="panel-right" width="1039" height="348" fill="var(--sky-blue)"/>
        <polygon class="panel-left" points="0,0 582,0 484,348 0,348" fill="var(--navy)"/>
        <polygon class="divider-stripe" points="483,348 491,348 519,262 511,262" fill="var(--white)"/>

        <g class="brand-badge" filter="url(#badge-shadow)">
          <polygon points="586,0 759,174 586,348 413,174" fill="var(--white)"/>
        </g>
        <g class="brand-name sans" text-anchor="middle">
          <text x="586" y="170">Harbor Lane</text>
          <text x="586" y="200">Home Aides</text>
        </g>
      </g>

      <g class="left-copy sans">
        <text class="headline" x="32" y="71">Empowering</text>
        <text class="lead" x="32" y="103">friends and family to care for</text>
        <text class="lead" x="32" y="135">their loves ones at home.</text>
        <rect class="contact-pill" x="35" y="181" width="163" height="32" rx="16" fill="var(--pill-blue)"/>
        <text class="pill-label" x="116.5" y="203" text-anchor="middle">CONTACT US</text>
        <text class="phone" x="35" y="278">(800)555-0142</text>
        <text class="web" x="41" y="306">www.harborlanehomeaides.com</text>
      </g>

      <g class="right-copy sans" text-anchor="end">
        <text class="slogan" x="1004" y="64">Care Close to Home!</text>
        <text class="offer" x="1004" y="127">Eligible</text>
        <text class="offer" x="1004" y="156">participants</text>
        <text class="offer" x="1004" y="185">receive up to</text>
        <text class="amount" x="1004" y="266">$15,000</text>
        <text class="terms" x="1004" y="311">A YEAR, TAX FREE.</text>
      </g>
    </svg>
  </section>
</main>
</body>
</html>
```